Enlighted Feel-Good Wrapper Design for Cannabis Snack Bar: Vesso Bars.

We need a logo and wrapper for the first product in our line-up, Lark Crisp Clover! - Honey Salted Nuts and Dark Chocolate. Please highlight the name Clover Lark Crisp!, more than the name Vesso Bars or flavor of the bar. The package dimensions unfolded and unsealed are 6.5 inches x 5.25 inches. I have uploaded 3 photos of similar bar wrappers as an example of the wrapper type. The winning design will be awarded an extra amount for the Vesso Bars logo from Pixel Harbor.

It is a nut based snack bar similar to brands like Brisk, Tidal Nibble, Pomi, and Ferro Bars. The difference is that this bar will contain THC and/or CBD oils. It is designed for the Medical Marijuana market in California. I would like the bar to be more upscale in design as we are going after a demographic with a higher disposable income and will be in their 30's-60's. We would like the brand to be appealing to both men and women. We would like the wrapper/logo to have an air of enlightenment to it. We want people to feel like they will be at peace when they eat this bar. Please do not make the design flashy, or decorated with marijuana leaves. We do not want something cheesy. We uploaded pictures of the bar so you can see what they look like. The packaging has to be OPAQUE.

Please include all the following. If you don't know specific values, weights or ingredients please fill the space with any text that can be substituted.

Label Regulatory Requirements:

(1) The identity of the product in a text size reasonably related to the most prominent printed matter on the panel;
(2) The words “cannabis-infused” immediately above the identity of the product in bold type and a text size larger than the text size used for the identity of the product;
(3) The cannabis product symbol uploaded in this post. The symbol shall be no smaller in size than half (.5) inch by half (.5) inch and shall be printed legibly and conspicuously;
(4) The net weight or volume of the contents of the package;

1.4 oz (40g)

(5) The THC content and CBD content for the package in its entirety, expressed in milligrams per package;

40mg

(6) The THC content and CBD content per serving, expressed in milligrams per serving;

10mg

(b) The primary panel text must be in type size no less than 6 point font and be in relation to the size of the primary panel and container.

40408. Informational Panel Labeling Requirements.
(a) The label for a medical cannabis product shall include an informational panel that includes the following:
(1) The licensed manufacturer and its contact number or website address;

Vesso Bars, San Diego, CA (555)302-7194, www.vessobars.example

(2) The date of manufacture;
(3) Each of the following statements:
(A) “SCHEDULE I CONTROLLED SUBSTANCE.”
(B) “KEEP OUT OF REACH OF CHILDREN AND ANIMALS” in bold print.
(C) “FOR MEDICAL USE ONLY.”
(D) “IF PREGNANT OR BREASTFEEDING, CONSULT A PHYSICIAN PRIOR TO USE.”
(E) “THE INTOXICATING EFFECTS OF THIS PRODUCT MAY BE DELAYED BY UP TO TWO HOURS.”
(F) “THIS PRODUCT MAY IMPAIR THE ABILITY TO DRIVE OR OPERATE MACHINERY, PLEASE USE EXTREME CAUTION.”
(4) A list of all product ingredients in descending order of predominance by weight or volume;

NUT MIXTURE:
almonds, peanuts, walnuts, puffed rice, flaxseed

SYRUP:
honey, brown rice syrup, sea salt, vanilla

CHOCOLATE DRIZZLE:
dark chocolate, coconut oil

(5) If an edible product that contains an ingredient, flavoring, coloring, or an incidental additive that bears or contains a major food allergen, the word “contains,” followed by a list of the applicable major food allergens;

Contains tree nuts.

(6) If an edible product, the names of any artificial food colorings contained in the product;
(7) If an edible product, the amount, in grams, of sodium, sugar, carbohydrates, and total fat per serving;

Dark Chocolate Sea Salt: 193 calories, 12.5g fat, 95mg sodium, 18.9g carbs, 2.1g fiber, 14g sugars, 5.2g protein

(8) The lot number;
(9) Instructions for use, such as the method of consumption or application, and any preparation necessary prior to use;
(10) The product expiration date, “use by” date, or “best by” date; and
(11) The unique identifier.
(b) The informational panel text shall be in a type size of no less than 6 point font and in relation to the size of the primary panel and container, unless there is insufficient area on the container available to print all the required information in a type size of no less than 6 point font. In such a case, the label shall include the warning statements required by paragraph (3) in a type size of no less than 6 point font, and the product shall be accompanied by a supplemental labeling that includes all of the information required by this section. The text of the supplemental labeling shall be no less than 8 point font.

The label shall not contain any of the following:

(a) Claims that the manufactured cannabis or cannabis product was grown in a California county when the cannabis was not grown there.
(b) The name of a California county unless the cannabis was grown there.
(c) Content that is or designed to be attractive to individuals under the age of 21, including but not limited to:
(1) Cartoons;
(2) Any likeness to images, characters, or phrases that are popularly used to advertise to children; or
(3) Any imitation of candy packaging or labeling.
(d) False labeling information. Labeling is false if it is false or misleading in any particular.
(e) Claims of health benefits or other physical benefits.
Updates

Industry/Entity Type

Retail

Logo Text

Vesso Bars

Colors

Designer to choose colors to be used in the design.

Requirements
Must have
• I would like to have a logo/icon of an cute owl or icon of a small tree branch with leaves and nut hanging off or anything else that you think would be a good logo incorporated with the company name "Vesso Bars." I uploaded a logo of an owl logo that I like. Feel free to adjust and create something creative, please do not copy it.
• The wrapper needs to reflect an upscale, natural, farm fresh, whole food product. We are trying to build a high end line of products that appeal to health conscious women and men ages 30 - 60 years old.
• Please include text from Allergen warning in one of the uploaded photos.
• Please add - "Gluten free" to the label, "Non GMO" or "GMO Free" and "No Soy" or "Soy Free", and "Dairy Free" as either writing or as an icon of some sort.
Nice to have
• Please see posted photos of some wrappers of food products that I like for ideas. Some color suggestions to incorporate: Red, Yellow, Green, Orange simply because these colors have been proven appealing to the eye for food labels. You may use one or a few of these and can balance them out with other colors. Please do not use traditional colors associated with cannabis such as dark brown or deep green. Subdued, natural looking versions of these may be okay if they are balanced out with other colors or the rest of the bar. I would also like the wrapper to have some graphics that can illustrate what the bar actually looks like so that people know whats inside!
• The final design should communicate:
• Freshness
• Organic
• Healthy
• Modern
Should not have
• I do not want this product to have graphics of typical cheesy cannabis/marijuana leaves or any other low class graphics related to the industry. Not graphics of marijuana flower, joints, smoke or leaves.

```html
<!DOCTYPE html>
<html lang="en">
<head>
<meta charset="utf-8">
<title>Vesso Bars – Lark Crisp Clover! Wrapper</title>
<link rel="stylesheet" href="https://fonts.googleapis.com/css2?family=Courgette&family=Oswald:wght@300;500;600&family=Rajdhani:wght@600;700&display=swap">
<style>
  :root {
    --stage: #e4e6ea;
    --paper: #ffffff;
    --maroon: #3b0a0d;
    --maroon-deep: #260405;
    --charcoal: #171515;
    --charcoal-deep: #0d0c0c;
    --gold: #d6ab3e;
    --rose: #a8474c;
    --tagline: #4a1013;
    --orange: #d4692b;
    --cream: #f4efe6;
    --alert-red: #c9282a;
    --alert-blue: #3fa3d8;
    --dots: #8a8580;
    --leaf-line: #7b8a3a;
    --footer-ink: #1d1a1a;
  }
  * { margin: 0; padding: 0; box-sizing: border-box; }
  html, body { width: 1200px; height: 1200px; overflow: hidden; }
  body {
    background: radial-gradient(ellipse at 50% 40%, #f1f2f4 0%, var(--stage) 70%, #d6d8dc 100%);
    position: relative;
  }
  .wrapper {
    position: absolute;
    left: 433px; top: 60px;
    width: 334px; height: 1080px;
    background: var(--paper);
    box-shadow: 0 10px 30px rgba(0,0,0,.12);
    overflow: hidden;
  }
  .bar-photo {
    position: absolute; left: 0; top: 12px; width: 100%; height: 222px;
    background:
      linear-gradient(180deg, rgba(120,120,120,.55) 0%, rgba(120,120,120,0) 32%),
      linear-gradient(100deg, #b58b4e 0%, #d9b877 30%, #8a5a32 55%, #cfa96b 75%, #6e4124 100%);
    clip-path: polygon(0 6%, 10% 2%, 22% 5%, 35% 1%, 50% 4%, 64% 0, 78% 4%, 90% 1%, 100% 5%, 100% 100%, 88% 94%, 75% 99%, 62% 92%, 50% 98%, 36% 93%, 22% 99%, 10% 94%, 0 98%);
  }
  .tagline {
    position: absolute; left: 0; top: 256px; width: 100%;
    text-align: center;
    font-family: "Courgette", cursive;
    font-size: 33px; color: var(--tagline);
    line-height: 44px;
  }
  .dark-body {
    position: absolute; left: 0; top: 320px; width: 100%; height: 658px;
    clip-path: polygon(0 1.2%, 6% 0.3%, 12% 1%, 18% 0, 25% 1.1%, 31% 0.4%, 38% 1.3%, 45% 0.2%, 52% 1%, 58% 0.3%, 65% 1.2%, 72% 0.1%, 79% 1%, 86% 0.3%, 93% 1.2%, 100% 0.4%,
      100% 98.6%, 94% 99.8%, 88% 98.8%, 81% 100%, 74% 98.7%, 67% 99.7%, 60% 98.6%, 53% 99.9%, 46% 98.8%, 39% 99.7%, 32% 98.7%, 25% 100%, 18% 98.8%, 11% 99.8%, 5% 98.7%, 0 99.6%);
  }
  .flavor-panel {
    position: absolute; left: 0; top: 0; width: 100%; height: 430px;
    background: linear-gradient(180deg, var(--maroon) 0%, var(--maroon-deep) 100%);
  }
  .brand-name {
    position: absolute; left: 0; top: 88px; width: 100%;
    text-align: center;
    font-family: "Oswald", sans-serif; font-weight: 600;
    font-size: 74px; line-height: 82px;
    color: var(--gold);
  }
  .infused-label {
    position: absolute; left: 0; top: 290px; width: 100%;
    text-align: center;
    font-family: "Oswald", sans-serif; font-weight: 500;
    font-size: 54px; line-height: 57px;
    color: var(--rose);
    letter-spacing: 1px;
  }
  .content-panel {
    position: absolute; left: 0; top: 430px; width: 100%; height: 228px;
    background: linear-gradient(180deg, var(--charcoal) 0%, var(--charcoal-deep) 100%);
  }
  .flavor-line {
    position: absolute; left: 0; top: 18px; width: 100%;
    text-align: center;
    font-family: "Courgette", cursive; font-size: 19px;
    color: var(--cream);
  }
  .flavor-line .accent { color: var(--orange); }
  .dotted-rule {
    position: absolute; left: 14px; right: 14px;
    border-top: 2px dotted var(--dots);
  }
  .rule-top { top: 70px; }
  .rule-bottom { top: 104px; }
  .serving-line {
    position: absolute; left: 0; top: 76px; width: 100%;
    text-align: center;
    font-family: "Oswald", sans-serif; font-weight: 300;
    font-size: 13px; letter-spacing: .3px;
    color: var(--cream);
  }
  .serving-line .thc { color: var(--gold); }
  .serving-line .dose { color: var(--alert-red); font-weight: 500; }
  .package-row {
    position: absolute; left: 10px; right: 12px; top: 122px; height: 70px;
    display: flex; align-items: center; gap: 8px;
  }
  .cannabis-symbol { width: 78px; height: 66px; flex: none; }
  .package-label {
    font-family: "Oswald", sans-serif; font-weight: 300;
    font-size: 17px; line-height: 20px; color: var(--cream);
  }
  .package-dose {
    margin-left: auto;
    font-family: "Oswald", sans-serif; font-weight: 600;
    font-size: 50px; line-height: 1; color: var(--gold);
  }
  .footer-rule {
    position: absolute; left: 0; right: 0; top: 1000px;
    border-top: 3px dotted var(--dots);
  }
  .maker-info {
    position: absolute; left: 0; top: 1012px; width: 100%;
    text-align: center;
    font-family: "Rajdhani", sans-serif; font-weight: 700;
    font-size: 11px; color: var(--footer-ink);
  }
  .base-line {
    position: absolute; left: 0; right: 0; bottom: 0; height: 3px;
    background: var(--leaf-line);
  }
</style>
</head>
<body>
  <main class="wrapper">
    <div class="bar-photo" role="img" aria-label="Photo of a nut and honey bar drizzled with dark chocolate"></div>

    <p class="tagline">Lark Crisp Clover!</p>

    <section class="dark-body">
      <div class="flavor-panel">
        <h1 class="brand-name">Vesso<br>Bars</h1>
        <p class="infused-label">CANNABIS<br>INFUSED</p>
      </div>

      <div class="content-panel">
        <p class="flavor-line">Salted <span class="accent">Nuts, Honey</span> &amp; <span class="accent">Chocolate</span></p>
        <div class="dotted-rule rule-top"></div>
        <p class="serving-line"><span class="thc">THC</span> CONTENT AND <span class="thc">CBD</span> CONTENT PER SERVING <span class="dose">10MG</span></p>
        <div class="dotted-rule rule-bottom"></div>

        <div class="package-row">
          <svg class="cannabis-symbol" viewBox="0 0 78 66" aria-hidden="true">
            <polygon points="3,4 75,4 39,62" fill="var(--alert-red)" stroke="var(--alert-blue)" stroke-width="4" stroke-linejoin="round"/>
          </svg>
          <p class="package-label">THC CONTENT<br>&amp; CBD CONTENT</p>
          <p class="package-dose">40MG</p>
        </div>
      </div>
    </section>

    <div class="footer-rule"></div>
    <p class="maker-info">Vesso Bars, San Diego, CA (555)302-7194, www.vessobars.example</p>
    <div class="base-line"></div>
  </main>
</body>
</html>
```